fully distributed
Project: fully distributed
fully distributed  - Information Technology
Creative Brief
Use specific fonts
calibri
Simple
Doug Pelliver
CMO
482 Corwin St , Floor 6 New York NY 10019
doug.pelliver@tulvaro.com
logo only
marcste marcste
on 18 and 19 can you fade the grey a litle so it just looks like a faint color
Xpert Xpert
Sure Sir.
we like some of yr designs can u try the design of 17 with the physical layout of card 2
like what you have started will check each one out
thanks we are looking for stationary too
please add fax number 1 800 937 2584

```html
<!DOCTYPE html>
<html lang="en">
<head>
<meta charset="utf-8">
<title>tulvaro — business card</title>
<link rel="stylesheet" href="https://fonts.googleapis.com/css2?family=Carlito:wght@400;700&display=swap">
<style>
  :root {
    --backdrop: #d9d9db;
    --card: #fbfbfb;
    --red: #e8323f;
    --red-faint: #f6d3d6;
    --ink: #1d1d1f;
    --grey: #7a7a7a;
  }
  * { box-sizing: border-box; margin: 0; padding: 0; }
  html, body { width: 1200px; height: 799px; overflow: hidden; }
  body {
    background: var(--backdrop);
    font-family: "Carlito", "Calibri", sans-serif;
    display: flex;
    align-items: center;
    justify-content: center;
    gap: 44px;
  }
  .card {
    position: relative;
    width: 520px;
    height: 297px;
    background: var(--card);
    overflow: hidden;
    box-shadow: 0 6px 18px rgba(0,0,0,.18);
  }
  .edge-bar { position: absolute; height: 7px; display: flex; }
  .edge-bar span { display: block; height: 100%; }
  .edge-bar .red { background: var(--red); }
  .edge-bar .black { background: var(--ink); }
  .edge-bar.top { top: 0; }
  .edge-bar.bottom { bottom: 0; }

  .faint-motif {
    position: absolute;
    border-radius: 50%;
    background: radial-gradient(circle, var(--red-faint) 0%, rgba(246,211,214,.45) 55%, rgba(246,211,214,0) 72%);
  }

  .wordmark {
    display: flex;
    align-items: center;
    gap: 8px;
    color: var(--ink);
    font-weight: 700;
    letter-spacing: -0.5px;
    line-height: 1;
  }
  .wordmark .dot {
    background: var(--red);
    border-radius: 50%;
    flex: none;
  }
  .tagline {
    font-weight: 700;
    color: var(--ink);
    white-space: nowrap;
  }

  /* front */
  .front .person {
    position: absolute;
    left: 40px;
    top: 78px;
    width: 170px;
    text-align: right;
  }
  .front .person-name { color: var(--red); font-size: 20px; }
  .front .person-role { color: var(--grey); font-size: 11px; margin-top: 3px; }
  .front .brand { position: absolute; right: 34px; top: 86px; text-align: right; }
  .front .wordmark { font-size: 50px; justify-content: flex-end; }
  .front .wordmark .dot { width: 12px; height: 12px; }
  .front .tagline { font-size: 13px; margin-top: 4px; }
  .front .contact {
    position: absolute;
    right: 34px;
    bottom: 30px;
    list-style: none;
    text-align: right;
    color: var(--red);
    font-size: 9.5px;
    line-height: 1.45;
  }
  .front .contact li { display: flex; justify-content: flex-end; align-items: center; gap: 5px; }
  .front .contact .gap { margin-top: 5px; }
  .front .contact svg { width: 9px; height: 9px; flex: none; }

  /* back */
  .back .brand { position: absolute; left: 46px; top: 100px; }
  .back .wordmark { font-size: 76px; }
  .back .wordmark .dot { width: 16px; height: 16px; }
  .back .tagline { font-size: 17px; margin-top: 4px; text-align: right; }
</style>
</head>
<body>

  <section class="card front">
    <div class="edge-bar top" style="left:0"><span class="red" style="width:250px"></span><span class="black" style="width:50px;margin-left:8px"></span></div>
    <div class="faint-motif" role="img" aria-label="Faint brand motif decoration" style="left:30px;top:-10px;width:170px;height:170px"></div>

    <div class="person">
      <p class="person-name">Doug Pelliver</p>
      <p class="person-role">CMO</p>
    </div>

    <div class="brand">
      <div class="wordmark"><span>tulvaro</span><span class="dot"></span></div>
      <p class="tagline">The Openly Networked Platform</p>
    </div>

    <ul class="contact">
      <li>482 Corwin St , Floor 6</li>
      <li>New York NY 10019
        <svg viewBox="0 0 10 10"><circle cx="5" cy="5" r="5" fill="#e8323f"/><circle cx="5" cy="4.2" r="1.6" fill="#fff"/></svg></li>
      <li class="gap">+1 212 555 0148
        <svg viewBox="0 0 10 10"><circle cx="5" cy="5" r="5" fill="#e8323f"/><path d="M3.3 2.8l1 1-.5.7c.4.8 1 1.4 1.8 1.8l.7-.5 1 1-.6.8C5 7.4 2.8 5.2 2.5 3.4z" fill="#fff"/></svg></li>
      <li>+1 800 937 2584
        <svg viewBox="0 0 10 10"><circle cx="5" cy="5" r="5" fill="#e8323f"/><rect x="2.7" y="3.4" width="4.6" height="3.4" fill="#fff"/></svg></li>
      <li class="gap">doug.pelliver@tulvaro.com
        <svg viewBox="0 0 10 10"><circle cx="5" cy="5" r="5" fill="#e8323f"/><path d="M2.6 3.4h4.8v3.3H2.6z M2.6 3.4L5 5.3l2.4-1.9" fill="none" stroke="#fff" stroke-width=".8"/></svg></li>
    </ul>

    <div class="edge-bar bottom" style="right:0"><span class="black" style="width:50px;margin-right:8px"></span><span class="red" style="width:230px"></span></div>
  </section>

  <section class="card back">
    <div class="edge-bar top" style="right:0"><span class="black" style="width:50px;margin-right:8px"></span><span class="red" style="width:190px"></span></div>
    <div class="faint-motif" role="img" aria-label="Faint brand motif decoration" style="left:120px;top:70px;width:240px;height:240px"></div>

    <div class="brand">
      <div class="wordmark"><span>tulvaro</span><span class="dot"></span></div>
      <p class="tagline">The Openly Networked Platform</p>
    </div>

    <div class="edge-bar bottom" style="left:0"><span class="black" style="width:50px;margin-right:8px"></span><span class="red" style="width:160px"></span></div>
  </section>

</body>
</html>
```